Financial Retirement Seminar Mailer

We would like to redesign our mailer flyer so that it looks classier and more effective in attracting people to sign up for our events. We help people who are near or in retirement achieve their financial goals.

PLEASE CHANGE THE ENTIRE FORMAT OF THE FLYER AND DO NOT LET IT LOOK SIMILAR TO WHAT WE CURRENTLY HAVE. NOTHING HAS TO STAY THE SAME. THE MORE UNIQUE YOU ARE THE HIGHER YOUR CHANCES OF WINNING.
ALL IMAGES CAN BE CHANGED (except Dorian Feld's photo and the logo for Marlow's Hearth Restaurant)

Target Market(s)

Our Target Market are upper middle class adults nearing or in retirement ages 55+.

Industry/Entity Type

Finance

Font styles to use
Serif
Sans Serif

Colors
0255a3
fece3e
ffffff

Requirements
Must have
• -Must have a photo of Dorian Feld and logo of Marlows Hearth. All other images can be changed.
• -Use our company colors which are navy and GOLD (Please use gold gradients instead of just yellow color)
• -The flyer must be folded in half. The inside can be full page.
Nice to have
• -If you could make the gold color stand out somehow maybe a gradient gold.

```html
<!DOCTYPE html>
<html lang="en">
<head>
<meta charset="utf-8">
<title>Dining and Retirement Education Mailer</title>
<link href="https://fonts.googleapis.com/css2?family=Cinzel:wght@400;500&family=Marcellus&family=Source+Sans+3:wght@400;600&display=swap" rel="stylesheet">
<style>
  :root{
    --navy:#1d3c7a;
    --navy-deep:#132b5e;
    --blue:#0255a3;
    --gold:#fece3e;
    --gold-dark:#c28e1c;
    --gold-grad:linear-gradient(90deg,#b98517 0%,#f6d56e 35%,#fece3e 55%,#d59f28 80%,#b07a12 100%);
    --paper:#ffffff;
    --mist:#f1f1f1;
    --ink:#1a1a2e;
    --bg:#e6e6e8;
  }
  *{box-sizing:border-box;margin:0;padding:0}
  html,body{width:1200px;height:802px;overflow:hidden;background:var(--bg)}
  body{position:relative;font-family:"Source Sans 3",sans-serif}
  .page{position:absolute;top:90px;width:460px;height:636px;overflow:hidden;box-shadow:0 4px 14px rgba(0,0,0,.25)}
  .page--cover{left:119px;background:var(--navy)}
  .page--inside{left:619px;background:var(--paper)}
  .page svg.shapes{position:absolute;inset:0}
  .abs{position:absolute}
  .center{left:0;right:0;text-align:center}
  .serif-caps{font-family:"Cinzel",serif;font-weight:400}
  .serif{font-family:"Marcellus",serif;font-weight:400}

  /* cover */
  .badge{left:20px;top:128px;width:98px;height:98px;border-radius:50%;background:var(--gold-grad);
    color:#fff;font-size:6.3px;font-weight:600;text-align:center;line-height:1.55;padding-top:22px;
    box-shadow:0 0 0 3px #e8b735}
  .badge svg{display:block;margin:0 auto 4px}
  .cover-title{top:243px;color:#fff;font-size:19px;letter-spacing:.2px}
  .cover-sub{top:265px;color:#fff;font-size:15px}
  .rule{top:288px;left:15px;right:15px;height:1px;background:rgba(255,255,255,.55)}
  .date-line{top:300px;color:var(--gold);font-size:10px}
  .address-line{top:315px;color:var(--gold);font-size:8px}
  .dash{top:308px;height:0;border-top:1px dashed rgba(255,255,255,.7)}
  .host-heading{top:337px;color:#fff;font-size:26px}
  .host-photo{left:331px;top:372px;width:120px;height:120px;border-radius:50%;
    background:radial-gradient(circle at 50% 40%,#d9d4cf 0%,#9a9aa0 55%,#2b2b35 100%);
    border:4px solid #fff;box-shadow:0 0 0 3px var(--gold-dark)}
  .host-name{left:13px;top:425px;color:#e8a912;font-size:16px}
  .host-bio{left:13px;top:446px;width:306px;color:var(--ink);font-size:8.2px;line-height:1.33}
  .host-bio p{margin-bottom:9px}
  .host-card{left:322px;top:498px;width:138px;text-align:center}
  .host-card .name{color:#e8a912;font-size:15px}
  .host-card .roles{color:var(--blue);font-size:7.4px;line-height:1.3;margin-top:5px}
  .press{left:16px;top:565px;display:flex;gap:16px;align-items:center}
  .press span{display:block;height:24px;background:#b6b6bc;border-radius:3px}
  .footer{left:0;right:0;top:600px;height:36px;background:var(--gold-grad);text-align:center;color:#fff}
  .footer .cta{font-size:12px;font-weight:600;padding-top:4px;letter-spacing:.1px}
  .footer .contact{font-size:7.6px;font-weight:600;display:flex;justify-content:center;gap:8px;align-items:center;margin-top:1px}
  .footer svg{vertical-align:-1px;margin-right:2px}

  /* inside */
  .in-title{top:27px;color:var(--navy);font-size:19px}
  .in-sub{top:51px;color:var(--navy);font-size:13px}
  .in-rule{top:84px;left:15px;right:15px;height:1px;background:var(--gold)}
  .invite{top:98px;left:22px;right:22px;text-align:center;color:var(--navy-deep);font-size:8.2px;line-height:1.55}
  .nosell{top:162px;color:var(--navy-deep);font-size:8.2px}
  .pill{left:54px;top:198px;width:350px;height:32px;border-radius:16px;background:var(--gold-grad);
    color:#fff;text-align:center;font-size:10px;font-weight:600;line-height:1.35;padding-top:3px;
    box-shadow:0 2px 4px rgba(0,0,0,.3)}
  .menu{top:240px;color:var(--gold);font-size:10px;font-weight:600}
  .day{top:283px;width:140px;text-align:center;color:#fff;font-size:14px;line-height:1.3}
  .divider{top:265px;width:1px;height:74px;background:rgba(254,206,62,.6)}
  .venue{left:150px;top:268px;width:160px;text-align:center;color:#fff}
  .venue .brand{display:inline-flex;align-items:center;gap:6px;font-size:12px;font-weight:600;letter-spacing:.4px;margin-top:12px}
  .venue .brand i{display:inline-block;width:10px;height:10px;background:var(--gold)}
  .venue .addr{font-size:7.8px;line-height:1.25;margin-top:14px}
  .topics-title{top:380px;color:var(--navy);font-size:21px}
  .topic{top:413px;width:106px;text-align:center;overflow:hidden}
  .topic .disc{width:92px;height:92px;margin:0 auto;border-radius:50%;border:5px solid #dcdcde;box-shadow:0 1px 3px rgba(0,0,0,.2)}
  .topic h3{color:var(--blue);font-size:9.6px;font-weight:400;margin-top:16px;letter-spacing:.1px;white-space:nowrap}
  .topic p{width:100px;margin:4px auto 0;color:#333;font-size:7px;line-height:1.35;white-space:normal;overflow-wrap:break-word}
</style>
</head>
<body>

<section class="page page--cover">
  <svg class="shapes" width="460" height="636" viewBox="0 0 460 636">
    <defs>
      <linearGradient id="goldA" x1="0" x2="1"><stop offset="0" stop-color="#b98517"/><stop offset=".45" stop-color="#fece3e"/><stop offset="1" stop-color="#c28e1c"/></linearGradient>
      <linearGradient id="dish" x1="0" y1="0" x2="1" y2="1"><stop offset="0" stop-color="#e9e6e3"/><stop offset=".55" stop-color="#d7b78a"/><stop offset="1" stop-color="#c9c6c3"/></linearGradient>
      <radialGradient id="glow" cx=".5" cy=".55" r=".6"><stop offset="0" stop-color="#2a58a8"/><stop offset="1" stop-color="#1d3c7a"/></radialGradient>
    </defs>
    <rect width="460" height="636" fill="url(#glow)"/>
    <path role="img" aria-label="Seafood pasta dish with mussels, clams and lemon in a white bowl" d="M0 6H460V226C380 232 300 212 250 180C190 140 90 150 0 200Z" fill="url(#dish)"/>
    <rect width="460" height="6" fill="url(#goldA)"/>
    <path d="M0 420C150 382 300 366 460 370V380C300 377 150 392 0 430Z" fill="url(#goldA)"/>
    <path d="M0 430C150 392 300 377 460 380V600H0Z" fill="#f1f1f1"/>
  </svg>

  <div class="abs badge">
    <svg width="18" height="14" viewBox="0 0 18 14"><path d="M6 2L14 7L6 12Z" fill="#fff"/></svg>
    VIEW A VIDEO OF<br>DORIAN ONLINE &amp; REGISTER AT<br>RETIREWISECLASSES.ORG
  </div>

  <h1 class="abs center serif-caps cover-title">DINING AND RETIREMENT EDUCATION</h1>
  <p class="abs center serif cover-sub">By: Westbrook Instructor Dorian Feld</p>
  <div class="abs rule"></div>
  <div class="abs dash" style="left:-40px;width:60px"></div>
  <div class="abs dash" style="left:428px;width:40px"></div>
  <p class="abs center date-line">Tuesday - October 8th at 7:00 pm <b>OR</b> Wednesday - October 9th at 7:00 pm</p>
  <p class="abs center address-line">4800 Harborline Ave. #210 Bayview Shores, CA 90000 (Floor 2)</p>
  <h2 class="abs center serif-caps host-heading">MEET YOUR HOST</h2>

  <div class="abs host-photo" role="img" aria-label="Portrait of host Dorian Feld in a dark suit and gold tie"></div>
  <h3 class="abs serif host-name">Dorian Feld</h3>
  <div class="abs host-bio">
    <p>Dorian Feld is an instructor at Westbrook College and a Certified Financial Planner. Dorian writes for the Market Ledger and is a regular guest on KVRB 980AM. As an instructor Dorian's focus is on teaching about smart retirement strategies that are unknown to most consumers.</p>
    <p>His lectures are focused on retirement, estate planning and advanced tax strategies. Dorian works exclusively with people ages 55-67 years old who are in retirement or focused on retiring.</p>
    <p>Dorian has been featured in the following and more:</p>
  </div>
  <div class="abs host-card">
    <div class="serif name">Dorian Feld</div>
    <div class="roles">Certified Financial Planner<br>Instructor at Westbrook<br>Market Ledger Writer</div>
  </div>
  <div class="abs press" aria-label="Media features">
    <span style="width:46px"></span><span style="width:64px"></span><span style="width:56px"></span><span style="width:56px"></span><span style="width:26px;border-radius:50%;height:26px"></span>
  </div>

  <div class="abs footer">
    <div class="cta">REGISTRATION IS LIMITED! CONFIRM TODAY AT</div>
    <div class="contact">
      <span><svg width="8" height="8" viewBox="0 0 10 10"><path d="M2 1L4 1L5 3L4 4C4.6 5.3 5 5.7 6 6L7 5L9 6L9 8C6 9 1 4 2 1Z" fill="#fff"/></svg>555-014-2290 or visit</span>
      <span><svg width="8" height="8" viewBox="0 0 10 10"><circle cx="5" cy="5" r="4" fill="none" stroke="#fff" stroke-width="1.4"/></svg>retirewiseclasses.org</span>
    </div>
  </div>
</section>

<section class="page page--inside">
  <svg class="shapes" width="460" height="636" viewBox="0 0 460 636">
    <defs>
      <linearGradient id="goldB" x1="0" x2="1"><stop offset="0" stop-color="#b98517"/><stop offset=".45" stop-color="#fece3e"/><stop offset="1" stop-color="#c28e1c"/></linearGradient>
      <radialGradient id="glowB" cx=".5" cy=".4" r=".6"><stop offset="0" stop-color="#2a58a8"/><stop offset="1" stop-color="#1d3c7a"/></radialGradient>
    </defs>
    <rect width="460" height="6" fill="url(#goldB)"/>
    <rect y="214" width="460" height="386" fill="url(#glowB)"/>
    <path d="M0 404C130 350 320 338 460 420V432C320 350 130 362 0 414Z" fill="url(#goldB)"/>
    <path d="M0 414C130 362 320 350 460 432V600H0Z" fill="#f1f1f1"/>
  </svg>

  <h1 class="abs center serif-caps in-title">ADVANCED RETIREMENT SOLUTIONS</h1>
  <p class="abs center serif in-sub">Featuring Westbrook Instructor Dorian Feld, CFP</p>
  <div class="abs in-rule"></div>
  <p class="abs invite">You are invited to an educational talk featuring Westbrook Instructor Dorian Feld. This free* event is focused on teaching the techniques and tools that your financial advisor does not want you to know. Instructor Dorian Feld will cover advanced retirement and tax topics which are proven to be successful and mostly unknown to consumers.</p>
  <p class="abs center nosell">Leave your checkbooks at home, there will be no selling here!</p>

  <div class="abs pill">EARLY ENROLLMENT IS FREE.<br>Participants may enroll at door for $99 per seat.</div>
  <p class="abs center menu">Choose from: Vegan, Vegetarian, Seafood, Pasta or Steak</p>

  <div class="abs day" style="left:0">TUESDAY<br>October 8th<br>at 7:00 pm</div>
  <div class="abs divider" style="left:142px"></div>
  <div class="abs venue">
    <div class="brand"><i></i>MARLOW'S HEARTH</div>
    <div class="addr">4800 Harborline Ave. #210 Bayview Shores,<br>CA 90000 (Floor 2)</div>
  </div>
  <div class="abs divider" style="left:317px"></div>
  <div class="abs day" style="left:330px">WEDNESDAY<br>October 9th<br>at 7:00 pm</div>

  <h2 class="abs center serif-caps topics-title">TOPICS</h2>
  <div class="abs topic" style="left:12px">
    <div class="disc" role="img" aria-label="Hands reviewing financial charts with a calculator" style="background:linear-gradient(135deg,#eef1f5,#b9c6d8)"></div>
    <h3>LOW-RISK INVESTING</h3>
    <p>New low-risk investments that produce 5%-7% interest and can provide you long term care income. (Not Stocks/Bonds)</p>
  </div>
  <div class="abs topic" style="left:123px">
    <div class="disc" role="img" aria-label="Last will and testament document with a pen and gavel" style="background:linear-gradient(135deg,#f2efe9,#b98a5c)"></div>
    <h3>ESTATE PLANNING</h3>
    <p>If you own a home, it's essential to have a Trust in order to avoid probate and to protect yourself if you become disabled.</p>
  </div>
  <div class="abs topic" style="left:232px">
    <div class="disc" role="img" aria-label="Smiling retired couple outdoors" style="background:linear-gradient(135deg,#e4d6c6,#9db5cf)"></div>
    <h3>TAX STRATEGIES</h3>
    <p>Learn how to save at least 30% on your 401k taxes and greatly reduce your taxable income in retirement.</p>
  </div>
  <div class="abs topic" style="left:342px">
    <div class="disc" role="img" aria-label="Caregiver assisting a senior woman" style="background:linear-gradient(135deg,#eef2f6,#a9b8c9)"></div>
    <h3>LONG TERM CARE</h3>
    <p>Learn how to protect yourself against the high costs of long-term care. Discover 3 new solutions you may not have seen before.</p>
  </div>

  <div class="abs footer">
    <div class="cta">REGISTRATION IS LIMITED! CONFIRM TODAY AT</div>
    <div class="contact">
      <span><svg width="8" height="8" viewBox="0 0 10 10"><path d="M2 1L4 1L5 3L4 4C4.6 5.3 5 5.7 6 6L7 5L9 6L9 8C6 9 1 4 2 1Z" fill="#fff"/></svg>555-014-2290 or visit</span>
      <span><svg width="8" height="8" viewBox="0 0 10 10"><circle cx="5" cy="5" r="4" fill="none" stroke="#fff" stroke-width="1.4"/></svg>retirewiseclasses.org</span>
    </div>
  </div>
</section>

</body>
</html>
```